Business Card Design Project

We're an orthopaedic office, and our colors are blue white and balck. Dealing with physicians and healthcare execs, I'd like this card to have a classy, yet overpowering wow factor.

Here are a couple of cards I like that are close to what I'm looking for:
http://www.plumvantia.com/design/671583
http://www.plumvantia.com/design/514515

```html
<!DOCTYPE html>
<html lang="en">
<head>
<meta charset="utf-8">
<title>Crestline Orthopaedic – Business Card</title>
<link rel="stylesheet" href="https://fonts.googleapis.com/css2?family=Source+Sans+3:wght@400;600&display=swap">
<style>
  :root {
    --backdrop: #d9d9db;
    --card-blue: #263c9a;
    --card-blue-glow: #1d55b5;
    --card-grey-edge: #b9babd;
    --card-grey-center: #ffffff;
    --ink-white: #ffffff;
    --ink-dark: #1e1e22;
    --brand-blue: #2a3b9c;
  }
  * { margin: 0; padding: 0; box-sizing: border-box; }
  html, body {
    width: 1200px;
    height: 789px;
    overflow: hidden;
    background: var(--backdrop);
    font-family: "Source Sans 3", "Myriad Pro", Arial, sans-serif;
  }
  .canvas {
    position: relative;
    width: 1200px;
    height: 789px;
  }
  .card {
    position: absolute;
    width: 503px;
    height: 284px;
    box-shadow: 0 6px 18px rgba(0,0,0,0.25);
  }
  .card-front {
    left: 191px;
    top: 92px;
    background: radial-gradient(circle at 42% 48%, var(--card-blue-glow) 0%, var(--card-blue) 55%);
    color: var(--ink-white);
  }
  .card-back {
    left: 551px;
    top: 416px;
    background: radial-gradient(ellipse at 50% 50%, var(--card-grey-center) 0%, #ececed 35%, var(--card-grey-edge) 85%);
  }
  .brand {
    position: absolute;
    display: flex;
    align-items: center;
    gap: 10px;
  }
  .brand-dot {
    width: 30px;
    height: 30px;
    border-radius: 50%;
  }
  .brand-name {
    font-size: 25px;
    font-weight: 400;
    letter-spacing: 0.5px;
    line-height: 1;
  }
  .card-front .brand { left: 30px; top: 129px; }
  .card-front .brand-dot { background: var(--ink-white); }
  .card-front .brand-name { color: var(--ink-white); }
  .card-back .brand { left: 136px; top: 127px; }
  .card-back .brand-dot { background: var(--brand-blue); }
  .card-back .brand-name { color: var(--ink-dark); }

  .holder {
    position: absolute;
    left: 293px;
    top: 55px;
    font-size: 15px;
    line-height: 23px;
  }
  .contact {
    position: absolute;
    left: 293px;
    top: 193px;
    list-style: none;
    font-size: 13.5px;
    line-height: 17.5px;
  }
  .contact-item { display: flex; align-items: center; gap: 4px; }
  .contact-icon { width: 11px; height: 11px; flex: none; }
</style>
</head>
<body>
<main class="canvas">
  <section class="card card-front" aria-label="Card front">
    <div class="brand">
      <span class="brand-dot"></span>
      <span class="brand-name">CRESTLINE ORTHOPAEDIC</span>
    </div>
    <p class="holder">Darren Holloway -<br>CEO</p>
    <ul class="contact">
      <li class="contact-item">
        <svg class="contact-icon" viewBox="0 0 12 12" aria-hidden="true"><path d="M2.5 1h2l1 3-1.3 1a6 6 0 0 0 2.8 2.8L8 6.5l3 1v2a1.5 1.5 0 0 1-1.5 1.5A8.5 8.5 0 0 1 1 2.5 1.5 1.5 0 0 1 2.5 1z" fill="none" stroke="currentColor" stroke-width="1"/></svg>
        (555) 274-9130
      </li>
      <li class="contact-item">
        <svg class="contact-icon" viewBox="0 0 12 12" aria-hidden="true"><rect x="0.5" y="2" width="11" height="8" fill="none" stroke="currentColor"/><path d="M0.5 2 6 6.5 11.5 2M0.5 10 4.5 5.5M11.5 10 7.5 5.5" fill="none" stroke="currentColor"/></svg>
        dholloway@crestlineortho.com
      </li>
      <li>1820 Harbor Ridge Rd., Fairhaven,</li>
      <li>ST 00412</li>
    </ul>
  </section>

  <section class="card card-back" aria-label="Card back">
    <div class="brand">
      <span class="brand-dot"></span>
      <span class="brand-name">CRESTLINE ORTHOPAEDIC</span>
    </div>
  </section>
</main>
</body>
</html>
```